Brantley Invites you to Celebrate 50 Years with them

Email invitation using the attached logo files- design may also need to be converted to stationary.

Date: Tuesday May 15 2018
Time: 11 am - 1 pm
Where: Oak Hollow 4817 Garnet Lane Pigeon Forge TN 37841

Example: Brantley cordially Invites you to a luncheon to Celebrate 50 years of business!

* Use the colors in the logo to tie the invitation together

Target Market(s)

Business associates, vendors and leaders in community

Industry/Entity Type

Hospitality

Requirements
Must have
• logo attached and information provided in brief
Nice to have
• also be able to use as stationary
Should not have
• any additional images to purchase

```html
<!DOCTYPE html>
<html lang="en">
<head>
<meta charset="utf-8">
<title>Brantley Hospitality – 50th Anniversary Invitation &amp; Stationery</title>
<link rel="stylesheet" href="https://fonts.googleapis.com/css2?family=Merriweather:ital,wght@0,400;1,400&family=Open+Sans:wght@400&display=swap">
<style>
  :root {
    --brand-blue: #1374bd;
    --brand-grey: #a3a5a8;
    --paper: #ffffff;
    --ink: #2b2b2b;
    --backdrop: #e9e9ea;
    --rule: #c9c9c9;
    --shadow: rgba(0,0,0,0.18);
  }
  * { margin: 0; padding: 0; box-sizing: border-box; }
  html, body { width: 1200px; height: 1200px; overflow: hidden; }
  body { background: var(--backdrop); position: relative; font-family: "Merriweather", Georgia, serif; }

  .letterhead {
    position: absolute; left: 359px; top: 99px; width: 709px; height: 1002px;
    background: var(--paper);
  }
  .letterhead .brand-name { position: absolute; right: 60px; top: 75px; }
  .letterhead .footer {
    position: absolute; left: 170px; right: 170px; bottom: 36px;
    border-top: 1px solid var(--rule); padding-top: 18px;
    text-align: center; font-style: italic; font-size: 14px; color: var(--ink);
  }

  .invitation {
    position: absolute; left: 60px; right: 60px; top: 672px;
    text-align: center; color: var(--ink);
  }
  .invitation .lead { font-style: italic; font-size: 14px; line-height: 1.5; }
  .invitation .headline {
    margin-top: 10px; color: var(--brand-blue); font-size: 22px; line-height: 1.35;
  }
  .invitation .details {
    margin: 18px auto 0; display: flex; justify-content: center; gap: 34px;
    font-size: 12.5px; line-height: 1.6;
  }
  .invitation .details dt {
    color: var(--brand-grey); font-size: 10px; letter-spacing: 0.14em; text-transform: uppercase;
  }
  .invitation .details dd { margin: 0; }

  .brand-name {
    display: flex; align-items: center; gap: 8px;
    color: var(--brand-blue); font-family: "Merriweather", Georgia, serif;
    font-weight: 400; font-size: 16px; letter-spacing: 0.08em; text-transform: uppercase;
  }
  .brand-name .dot { width: 14px; height: 14px; border-radius: 50%; background: var(--brand-blue); flex: none; }

  .card { position: absolute; width: 321px; height: 185px; box-shadow: 18px 18px 22px var(--shadow); }
  .card-front {
    left: 132px; top: 303px; background: var(--paper);
    display: flex; flex-direction: column; align-items: center; justify-content: center;
  }
  .card-front .brand-name { font-size: 14px; margin-top: 14px; }
  .card-front .web {
    margin-top: 48px; font-family: "Open Sans", Arial, sans-serif; font-size: 11px; color: var(--ink);
  }

  .card-back { left: 434px; top: 547px; background: var(--brand-blue); color: var(--paper); }
  .card-back .brand-name {
    position: absolute; left: 44px; top: 56px; color: var(--paper); font-size: 9px;
  }
  .card-back .brand-name .dot { background: var(--paper); width: 9px; height: 9px; }
  .card-back .contact { position: absolute; right: 43px; top: 26px; text-align: right; font-style: italic; }
  .card-back .contact .person { font-size: 11.5px; line-height: 1.2; }
  .card-back .contact .phone { font-size: 9px; }
  .card-back .divider {
    position: absolute; left: 44px; right: 43px; top: 103px; border-top: 1px solid rgba(255,255,255,0.35);
  }
  .card-back .address {
    position: absolute; right: 43px; top: 111px; text-align: right;
    font-style: italic; font-size: 8.6px; line-height: 1.35;
  }
</style>
</head>
<body>
  <section class="letterhead">
    <div class="brand-name"><span class="dot"></span>Brantley Hospitality</div>

    <article class="invitation">
      <p class="lead">Brantley cordially invites you to a luncheon</p>
      <h1 class="headline">Celebrate 50 Years of Business</h1>
      <dl class="details">
        <div><dt>Date</dt><dd>Tuesday, May 15, 2018</dd></div>
        <div><dt>Time</dt><dd>11 am – 1 pm</dd></div>
        <div><dt>Where</dt><dd>Oak Hollow, 4817 Garnet Lane</dd></div>
      </dl>
    </article>

    <p class="footer">Oak Hollow 4817 Garnet Lane Pigeon Forge TN 37841</p>
  </section>

  <section class="card card-front">
    <div class="brand-name"><span class="dot"></span>Brantley Hospitality</div>
    <p class="web">www.brantleyhospitality.com</p>
  </section>

  <section class="card card-back">
    <div class="brand-name"><span class="dot"></span>Brantley</div>
    <div class="contact">
      <p class="person">Your Name</p>
      <p class="phone">123 456 7890</p>
    </div>
    <div class="divider"></div>
    <p class="address">Oak Hollow 4817<br>Garnet Lane<br>Pigeon Forge<br>TN 37841</p>
  </section>
</body>
</html>
```